We are seeking two label designs for our premium pecan snack brand, TORVELLO. TORVELLO is known for its innovative pecan snacks, specifically a healthy and exotic blend of pecans, expertly salted, and infused with unique chili flavors. Our snacks are packaged in stand-up pouch bags, and we are looking for label designs product sizes - 5 oz. ( Size: 14 x 20 cm / 5.5 x 7.8 inches / Max Capacity: 16.2 oz)

Background Information:
TORVELLO is a brand committed to offering a delightful snacking experience that combines the natural richness of pecans with the bold and exotic kick of carefully selected chilies. Our snacks cater to health-conscious consumers who appreciate the fusion of premium quality, unique flavors, and nutritional goodness.

Target Market(s)

Event Attendees (Entertainment Industry), Health-Conscious Consumers

Industry/Entity Type

Entertainment (sports events, arenas, stadiums, etc)

Font styles to use
Other font styles liked:
• Brother1816 Printed

Colors

Designer to choose colors to be used in the design.

Requirements
Must have
• Nutrition Fact (attached) , TRANSPARENT PART LIKE A WINDOW TO DISPLAY THE PRODUCT

```html
<!DOCTYPE html>
<html lang="en">
<head>
<meta charset="utf-8">
<title>TORVELLO Spicy Roasted Pecans – Pouch Label</title>
<link rel="stylesheet" href="https://fonts.googleapis.com/css2?family=Nunito:ital,wght@0,400;0,700;0,800;0,900;1,400&family=Fredoka:wght@600&display=swap">
<style>
  :root {
    --label-bg: #f1f1f1;
    --ink: #161616;
    --chili: #e0643a;
    --chili-deep: #c9471f;
    --pecan-dark: #6e3a22;
    --pecan-mid: #9a5a3a;
    --pecan-light: #c98a63;
    --muted: #3a3a3a;
  }
  * { margin: 0; padding: 0; box-sizing: border-box; }
  html, body {
    width: 1200px;
    height: 1200px;
    overflow: hidden;
    background: var(--label-bg);
  }
  .label {
    position: relative;
    width: 1200px;
    height: 1200px;
    background: var(--label-bg);
    font-family: "Nunito", sans-serif;
    color: var(--ink);
  }
  .brand-name {
    position: absolute;
    top: 90px;
    left: 0;
    width: 100%;
    text-align: center;
    font-family: "Nunito", sans-serif;
    font-weight: 900;
    font-size: 118px;
    letter-spacing: 4px;
    line-height: 1;
    color: var(--ink);
  }
  .product-type {
    position: absolute;
    top: 250px;
    left: 0;
    width: 100%;
    text-align: center;
    font-size: 34px;
    font-weight: 400;
    letter-spacing: 1.5px;
    color: var(--muted);
  }
  .premium-badge {
    position: absolute;
    top: 340px;
    left: 95px;
    width: 260px;
  }
  .premium-badge .premium-line {
    display: block;
    font-family: "Fredoka", sans-serif;
    font-weight: 600;
    font-size: 108px;
    line-height: 0.98;
    letter-spacing: 8px;
    color: var(--chili);
  }
  .premium-badge .premium-line:nth-child(1) { transform: rotate(-4deg); }
  .premium-badge .premium-line:nth-child(2) { padding-left: 22px; transform: rotate(3deg); }
  .premium-badge .premium-line:nth-child(3) { padding-left: 8px; }
  .premium-badge .quality {
    display: block;
    margin-top: 6px;
    padding-left: 10px;
    font-weight: 800;
    font-size: 40px;
    letter-spacing: 1.5px;
    color: var(--ink);
  }
  .rocket-illustration {
    position: absolute;
    top: 320px;
    left: 420px;
    width: 360px;
    height: 440px;
  }
  .features {
    position: absolute;
    top: 385px;
    left: 790px;
    width: 370px;
    list-style: none;
    text-align: center;
  }
  .features li {
    font-style: italic;
    font-weight: 400;
    font-size: 35px;
    line-height: 58px;
    color: var(--muted);
  }
  .product-window {
    position: absolute;
    top: 790px;
    left: 60px;
    width: 1080px;
    height: 250px;
  }
  .net-weight {
    position: absolute;
    top: 1070px;
    left: 0;
    width: 100%;
    text-align: center;
    font-weight: 800;
    font-size: 52px;
    line-height: 1;
    color: var(--chili);
  }
  .net-weight-metric {
    position: absolute;
    top: 1132px;
    left: 0;
    width: 100%;
    text-align: center;
    font-weight: 400;
    font-size: 34px;
    line-height: 1;
    color: var(--muted);
  }
</style>
</head>
<body>
  <main class="label">
    <h1 class="brand-name">TORVELLO</h1>
    <p class="product-type">SPICY ROASTED PECANS</p>

    <div class="premium-badge">
      <span class="premium-line">PRE</span>
      <span class="premium-line">MI</span>
      <span class="premium-line">UM</span>
      <span class="quality">QUALITY</span>
    </div>

    <svg class="rocket-illustration" viewBox="0 0 360 440" role="img" aria-label="Illustration of a pecan-half rocket launching with chili splashes and orange exhaust swirls">
      <defs>
        <radialGradient id="rocketFill" cx="50%" cy="45%" r="60%">
          <stop offset="0%" stop-color="#c98a63"/>
          <stop offset="60%" stop-color="#e0643a"/>
          <stop offset="100%" stop-color="#f1f1f1" stop-opacity="0"/>
        </radialGradient>
      </defs>
      <rect x="0" y="0" width="360" height="440" fill="url(#rocketFill)"/>
    </svg>

    <ul class="features">
      <li>expertly salted</li>
      <li>chili flavors</li>
      <li>innovative snack</li>
      <li>healthy and exotic</li>
    </ul>

    <svg class="product-window" viewBox="0 0 1080 250" preserveAspectRatio="none" role="img" aria-label="Transparent window showing roasted pecan halves inside the pouch">
      <defs>
        <linearGradient id="windowFill" x1="0" y1="0" x2="1" y2="1">
          <stop offset="0%" stop-color="#9a5a3a"/>
          <stop offset="45%" stop-color="#6e3a22"/>
          <stop offset="75%" stop-color="#9a5a3a"/>
          <stop offset="100%" stop-color="#6e3a22"/>
        </linearGradient>
      </defs>
      <rect x="0" y="0" width="1080" height="250" fill="url(#windowFill)"/>
    </svg>

    <p class="net-weight">net wt: 5 oz.</p>
    <p class="net-weight-metric">(142 gr.)</p>
  </main>
</body>
</html>
```